Welcome New Physician postcard mailer

We need a postcard design to welcome our new pediatric ophthalmologist to our practice. I will upload a picture and would like to the left of the postcard with a circular frame around picture. At the top, the header should be our business name. Juvenile Vision Partners and Household Sight Clinic. Our primary colors are red, yellow, and blue. I will forward a sample of another postcard we received for example. I will also send our magnets that give out.

Welcoming Dr. Meera Pashkin, M.D.
Pediatric Ophthalmologist

Juvenile Vision Partners and Household Sight Clinic is happy to announce the addition of Meera Pashkin, M.D. to our practice.

Dr. Pashkin received her medical degree at WRLB School of Medicine and completed an Internal Medicine internship and Ophthalmology Residency at Corliss Medical Center in New Orleans. She returns home to the Tulsa area to join pediatric ophthalmologist Dr. Frank Holbury, M.D., Dr. Paul Verdanti, D.O., and Dr. Rina Voss, M.D., after completing a fellowship in Pediatric Ophthalmology and Adult Strabismus at Harlow Sight Institute at WPSU.

Dr. Pashkin is a member of the National Guild of Ophthalmology and Strabismus. We and our patients are already appreciative of the pleasant demeanor and attentive care she brings to our practice.

Offices in Tulsa, BA, Owasso, Bartlesville, Muskogee and Miami

Call for Appointments: 918.555-0143

www.juvenilevisionpartners.example

On the back of the card list our multi location addresses and individual physicians:

Frank Holbury, M.D.
Paul Verdanti, D.O.
Rina Voss, M.D.
Meera Pashkin, M.D.
Doreen Pruitt, O.D.

2811 W 52nd St, Suite 300
Tulsa, Ok 74136
918.555-0143

7315 S Hollister Rd., Suite 210
Owasso, Ok 74055
918.555-0178

3208 S 4th St West
Broken Arrow, OK 74012
918.555-0192

Referring physicians

Medical

```html
<!DOCTYPE html>
<html lang="en">
<head>
<meta charset="utf-8">
<title>Postcard Back – Physicians and Locations</title>
<link rel="stylesheet" href="https://fonts.googleapis.com/css2?family=Roboto+Condensed:wght@400&display=swap">
<style>
  :root {
    --cream: #fffee2;
    --maroon: #780020;
    --maroon-text: #7a0a22;
    --olive-text: #6e4f08;
    --bullet: #6b4a0a;
    --gold-light: #ffe25a;
    --gold-dark: #f6c21c;
    --ink: #111111;
  }
  html, body {
    margin: 0;
    padding: 0;
    overflow: hidden;
    background: var(--cream);
  }
  .postcard {
    position: relative;
    width: 1200px;
    height: 923px;
    overflow: hidden;
    background: var(--cream);
    font-family: "Roboto Condensed", "Arial Narrow", sans-serif;
  }
  .info-panel-bg {
    position: absolute;
    left: 0;
    top: 0;
    width: 572px;
    height: 782px;
  }
  .panel-divider {
    position: absolute;
    left: 572px;
    top: 0;
    width: 6px;
    height: 742px;
    background: var(--maroon);
  }
  .section-title {
    position: absolute;
    margin: 0;
    font-weight: 400;
    white-space: nowrap;
  }
  .physicians-title {
    left: 178px;
    top: 20px;
    font-size: 40px;
    color: #ffffff;
  }
  .physician-list {
    position: absolute;
    left: 186px;
    top: 84px;
    margin: 0;
    padding: 0;
    list-style: none;
  }
  .physician-list li {
    height: 45.7px;
    font-size: 27px;
    color: var(--maroon-text);
    display: flex;
    align-items: center;
  }
  .physician-list .chevron {
    width: 27px;
    font-size: 22px;
    font-weight: 700;
  }
  .locations-banner {
    position: absolute;
    left: 97px;
    top: 325px;
    width: 370px;
    height: 67px;
    background: linear-gradient(180deg, var(--gold-light), var(--gold-dark));
    box-shadow: 0 6px 10px rgba(120, 80, 0, 0.3);
  }
  .locations-title {
    left: 0;
    right: 0;
    top: 9px;
    text-align: center;
    font-size: 39px;
    color: var(--maroon-text);
  }
  .location {
    position: absolute;
    margin: 0;
    font-style: normal;
    font-size: 26px;
    line-height: 34px;
    color: var(--olive-text);
    padding-left: 26px;
  }
  .location::before {
    content: "";
    position: absolute;
    left: 0;
    top: 12px;
    width: 13px;
    height: 13px;
    border-radius: 50%;
    background: var(--bullet);
  }
  .location .line { display: block; }
  .location .line + .line { margin-left: 0; }
  .location-tulsa { left: 36px; top: 405px; }
  .location-owasso { left: 82px; top: 519px; }
  .location-ba { left: 132px; top: 633px; }
  .postage-area {
    position: absolute;
    left: 975px;
    top: 75px;
    width: 136px;
    height: 136px;
    border: 2px solid var(--ink);
    background: #ffffff;
    display: flex;
    align-items: center;
    justify-content: center;
    text-align: center;
    font-family: Arial, Helvetica, sans-serif;
    font-size: 26px;
    line-height: 32px;
    color: var(--ink);
  }
  .address-line {
    position: absolute;
    left: 695px;
    width: 406px;
    height: 2px;
    background: var(--ink);
  }
</style>
</head>
<body>
<main class="postcard">
  <svg class="info-panel-bg" viewBox="0 0 572 782" aria-hidden="true">
    <defs>
      <linearGradient id="panelWarm" x1="0" y1="0" x2="1" y2="1">
        <stop offset="0" stop-color="#ffc27a"/>
        <stop offset="0.45" stop-color="#ffe6b0"/>
        <stop offset="1" stop-color="#fff6d2"/>
      </linearGradient>
    </defs>
    <path d="M0 0 H572 V740 H175 C150 740 135 770 110 782 H0 Z" fill="url(#panelWarm)"/>
    <path d="M0 0 H570 V75 H200 C165 75 150 118 110 118 H0 Z" fill="var(--maroon)"/>
    <path d="M0 118 H110 C150 118 165 75 200 75 H570" fill="none" stroke="#ffffff" stroke-width="2.5"/>
  </svg>

  <div class="panel-divider"></div>

  <h2 class="section-title physicians-title">Our Physiscians :</h2>
  <ul class="physician-list">
    <li><span class="chevron">›</span>Dr. Frank Holbury, M.D.</li>
    <li><span class="chevron">›</span>Dr. Paul Verdanti, D.O.</li>
    <li><span class="chevron">›</span>Dr. Rina Voss, M.D.</li>
    <li><span class="chevron">›</span>Dr. Meera Pashkin, M.D.</li>
    <li><span class="chevron">›</span>Dr. Doreen Pruitt, O.D.</li>
  </ul>

  <div class="locations-banner">
    <h2 class="section-title locations-title">Our Locations :</h2>
  </div>

  <address class="location location-tulsa">
    <span class="line">2811 W 52nd St, Suite 300</span>
    <span class="line">Tulsa, Ok 74136</span>
    <span class="line">918.555-0143</span>
  </address>
  <address class="location location-owasso">
    <span class="line">7315 S Hollister Rd., Suite 210</span>
    <span class="line">Owasso, Ok 74055</span>
    <span class="line">918.555-0178</span>
  </address>
  <address class="location location-ba">
    <span class="line">3208 S 4th St,(BA &amp; Kessler Lane exit)</span>
    <span class="line">Broken Arrow, OK 74012</span>
    <span class="line">918.555-0192</span>
  </address>

  <div class="postage-area">Postage<br>Area</div>

  <div class="address-line" style="top:441px"></div>
  <div class="address-line" style="top:512px"></div>
  <div class="address-line" style="top:582px"></div>
  <div class="address-line" style="top:653px"></div>
</main>
</body>
</html>
```